Child care/Preparatory Business Card Design & logo design

I need a logo to use on a business card, letterhead, uniform and promotional material for a new business called 'Kestrel Ridge Preparatory'. It is located in the north west of Western Australia in the Pilbara region. The service will provide a 'Foundations for Learning' program for 3 and 4 year old children. I would like a logo that shows unity, or belonging in children. I like the colour blue, any primary colours would be suitable. The design needs to be cheerful and appealing to children whilst still having an 'elite' edge to it.

Target Market(s)

Families with young children

Industry/Entity Type

Business

Contact Information for Business Card

Marcia Hollis Director
Kestrel Ridge Preparatory
M 0491 570 318
office@kestrelridgeprep.com.au
PO Box 581 Tarrent WA 6731

Foundations for Learning

```html
<!DOCTYPE html>
<html lang="en">
<head>
<meta charset="utf-8">
<title>Kestrel Ridge Preparatory — Stationery</title>
<link rel="stylesheet" href="https://fonts.googleapis.com/css2?family=Open+Sans:wght@400;600;700&display=swap">
<style>
  :root {
    --bg: #e9ecee;
    --paper: #ffffff;
    --aqua: #1fe9ec;
    --sky: #4fcdf3;
    --ink: #3a3a3a;
    --ink-soft: #555b60;
    --accent-red: #e5514f;
    --shadow: 0 4px 14px rgba(0,0,0,0.18);
  }
  * { box-sizing: border-box; margin: 0; padding: 0; }
  html, body { width: 1077px; height: 1200px; overflow: hidden; }
  body {
    background: var(--bg);
    font-family: "Open Sans", Arial, sans-serif;
    color: var(--ink);
    position: relative;
  }
  .sheet { position: absolute; background: var(--paper); box-shadow: var(--shadow); overflow: hidden; }

  .brand { display: flex; align-items: center; gap: 8px; }
  .brand-dot { width: 10px; height: 10px; border-radius: 50%; background: var(--accent-red); flex: none; }
  .brand-name { font-weight: 400; color: var(--ink); white-space: nowrap; }

  .tagline { font-size: 9px; color: var(--paper); text-align: center; white-space: nowrap; }

  .artwork { position: absolute; background: linear-gradient(160deg, rgba(31,233,236,0.35), rgba(31,233,236,0.15)); border-radius: 10px; }

  /* Letterhead */
  .letterhead { left: 560px; top: 30px; width: 487px; height: 690px; border-radius: 8px; }
  .letterhead .brand { position: absolute; left: 40px; top: 60px; }
  .letterhead .brand-name { font-size: 18px; }
  .letterhead .contact { position: absolute; right: 30px; top: 46px; text-align: right; font-size: 9.5px; line-height: 1.45; color: var(--ink-soft); font-style: normal; }
  .letterhead .contact strong { color: var(--ink); font-weight: 700; }
  .letterhead .rule { position: absolute; left: 0; right: 0; top: 112px; height: 3px; background: var(--aqua); }
  .letterhead .artwork { right: 26px; bottom: 46px; width: 150px; height: 170px; }
  .letterhead .foot { position: absolute; left: 0; right: 0; bottom: 0; height: 24px; background: var(--aqua); display: flex; align-items: center; justify-content: center; }

  /* Business cards */
  .card { width: 420px; height: 260px; border-radius: 16px; }
  .card-front { left: 50px; top: 40px; }
  .card-front .brand { position: absolute; left: 50%; top: 72px; transform: translateX(-50%); }
  .card-front .brand-name { font-size: 20px; }
  .card-front .holder { position: absolute; left: 0; right: 0; top: 128px; text-align: center; font-size: 13px; color: var(--ink-soft); }
  .card-front .band { position: absolute; left: 0; right: 0; bottom: 0; height: 92px; background: var(--sky); color: var(--paper); text-align: center; font-size: 9.5px; line-height: 1.5; padding-top: 18px; font-style: normal; }
  .card-back { left: 50px; top: 330px; background: var(--sky); }
  .card-back .artwork { right: 34px; top: 26px; width: 140px; height: 200px; background: rgba(255,255,255,0.28); }
  .card-back .tagline { position: absolute; left: 34px; bottom: 26px; text-align: left; }

  /* Envelope */
  .envelope { left: 30px; top: 760px; width: 1017px; height: 410px; border-radius: 10px; }
  .envelope .brand { position: absolute; left: 40px; top: 44px; }
  .envelope .brand-name { font-size: 18px; }
  .envelope .artwork { right: 70px; top: 110px; width: 190px; height: 230px; }
  .envelope .foot { position: absolute; left: 0; right: 0; bottom: 0; height: 30px; background: var(--aqua); display: flex; align-items: center; justify-content: center; }
</style>
</head>
<body>

<section class="sheet letterhead" aria-label="Letterhead">
  <div class="brand"><span class="brand-dot"></span><span class="brand-name">Kestrel Ridge Preparatory</span></div>
  <address class="contact">
    <strong>Marcia Hollis | Director</strong><br>
    0491 570 318<br>
    office@kestrelridgeprep.com.au<br>
    PO Box 581 Tarrent WA 6731
  </address>
  <div class="rule"></div>
  <div class="artwork" role="img" aria-label="Line drawing of a flower with a butterfly"></div>
  <div class="foot"><p class="tagline">Foundations for Learning</p></div>
</section>

<section class="sheet card card-front" aria-label="Business card front">
  <div class="brand"><span class="brand-dot"></span><span class="brand-name">Kestrel Ridge Preparatory</span></div>
  <p class="holder">Marcia Hollis | Director</p>
  <address class="band">
    0491 570 318<br>
    office@kestrelridgeprep.com.au<br>
    PO Box 581 Tarrent WA 6731
  </address>
</section>

<section class="sheet card card-back" aria-label="Business card back">
  <div class="artwork" role="img" aria-label="White line drawing of a flower with a butterfly"></div>
  <p class="tagline">Foundations for Learning</p>
</section>

<section class="sheet envelope" aria-label="Envelope">
  <div class="brand"><span class="brand-dot"></span><span class="brand-name">Kestrel Ridge Preparatory</span></div>
  <div class="artwork" role="img" aria-label="Line drawing of a flower with a butterfly"></div>
  <div class="foot"><p class="tagline">Foundations for Learning</p></div>
</section>

</body>
</html>
```